Motion Nest Business Cards

Can all designers please apply the following info on their designs' back-side of the business card: (please see brief file upload ('Info for backside...' - for required info, colours & layout)

SPECIALISING IN INDIVIDUAL PILATES INSTRUCTION
MATWORK – including small apparatus
and STUDIO:
VIVANTE 3 GLIDER
LADDER BARREL
COUNTOUR BARREL
FLEXI DOME
VIM STOOL
KIM-O-LAN

Business Cards for Motion Nest - applying the Motion Nest logo design selected earlier.
Note the business card requires both a front and back side. Please refer to two uploaded ppt-files for type of info required to be displayed, and rough position of where info could be. Require innovative / fresh approach to business card design and use of colour by designers now. Please refer to and use logo as uploaded - also for potential business card colour application.

Dear Designers,

Please note the additional inclusion / upload of two draft ppt-files that try to show where I want what type of information, for both the front & back sides of the required business card, plus an attempt at showing the high-level concept / idea of business info position.

As my 'drafts' obviously lack colour and any ability towards innovative card design or approach – I now rely on your vastly superior graphic design abilities to produce a really great business card for my business…

Looking forward to your submissions!

Kind regards, Merika for: Motion Nest 

Hello all Designers,

Can all designers please apply the following info on their designs' back-side of the business card: (please see / refer to the Brief and specifically the file upload ('Info for backside...' - for required info, colours & layout) - for the backside of the business card).

Info content (without colour, layout etc.):

and STUDIO:

VIVANTE 3 GLIDER

LADDER BARREL

COUNTOUR BARREL

FLEXI DOME

VIM STOOL

KIM-O-LAN

Thank you to all designers that submitted for consideration!

With regards,

Motion Nest

```html
<!DOCTYPE html>
<html lang="en">
<head>
<meta charset="utf-8">
<title>Motion Nest Business Card</title>
<link rel="stylesheet" href="https://fonts.googleapis.com/css2?family=PT+Sans:ital,wght@0,400;0,700;1,400&display=swap">
<style>
  :root {
    --backdrop: #e6e6e6;
    --slate: #46525a;
    --slate-text: #4a5560;
    --rose: #dc4d66;
    --paper: #f5f5f3;
    --white: #ffffff;
  }
  * { box-sizing: border-box; margin: 0; padding: 0; }
  html, body {
    width: 1200px;
    height: 900px;
    overflow: hidden;
    background: var(--backdrop);
    font-family: "PT Sans", Arial, sans-serif;
  }
  .sheet {
    position: relative;
    width: 1200px;
    height: 900px;
    display: flex;
    align-items: center;
    justify-content: center;
    gap: 40px;
  }
  .card {
    position: relative;
    width: 540px;
    height: 309px;
    box-shadow: 0 6px 18px rgba(0,0,0,0.18);
  }

  /* Back side */
  .card--back {
    background: var(--slate);
    color: var(--white);
    display: flex;
    flex-direction: column;
    align-items: center;
    justify-content: center;
  }
  .brand-lockup {
    display: flex;
    align-items: center;
    gap: 14px;
  }
  .brand-dot {
    width: 22px;
    height: 22px;
    border-radius: 50%;
    background: var(--rose);
  }
  .brand-name {
    font-size: 50px;
    font-weight: 400;
    letter-spacing: 0.5px;
    color: var(--white);
  }
  .tagline {
    margin-top: 22px;
    font-size: 14px;
    letter-spacing: 1.2px;
    color: var(--white);
  }

  /* Front side */
  .card--front {
    background: var(--paper);
    color: var(--slate-text);
  }
  .holder {
    position: absolute;
    left: 38px;
    top: 34px;
  }
  .holder-name {
    font-size: 25px;
    font-weight: 400;
    color: var(--slate-text);
    letter-spacing: 0.3px;
  }
  .holder-title {
    font-size: 14.5px;
    color: var(--rose);
    margin-top: 2px;
  }
  .contact {
    position: absolute;
    left: 38px;
    top: 122px;
    list-style: none;
    font-size: 14.5px;
  }
  .contact li {
    display: flex;
    align-items: center;
    gap: 12px;
    line-height: 20px;
  }
  .contact svg { width: 11px; height: 11px; flex: none; }
  .studio {
    position: absolute;
    left: 38px;
    top: 186px;
    font-size: 14.5px;
    line-height: 18px;
    font-style: normal;
  }
  .studio-label {
    color: var(--rose);
    font-weight: 700;
  }
  .front-mark {
    position: absolute;
    right: 34px;
    top: 168px;
    display: flex;
    align-items: center;
    gap: 10px;
  }
  .front-mark .brand-dot { width: 26px; height: 26px; }
  .front-mark-name {
    font-size: 30px;
    color: var(--rose);
    font-weight: 400;
  }
  .rule {
    position: absolute;
    height: 2px;
    background: var(--rose);
    top: 262px;
  }
  .rule--long { left: 0; width: 318px; }
  .rule--short { right: 0; width: 26px; }
  .website {
    position: absolute;
    right: 48px;
    top: 260px;
    font-size: 15px;
    color: var(--slate-text);
  }
</style>
</head>
<body>
<main class="sheet">

  <section class="card card--back" aria-label="Card back">
    <div class="brand-lockup">
      <span class="brand-dot"></span>
      <span class="brand-name">Motion Nest</span>
    </div>
    <p class="tagline">BALANCE • STRENGTH • FLEXIBILITY</p>
  </section>

  <section class="card card--front" aria-label="Card front">
    <header class="holder">
      <h1 class="holder-name">Merika Halvorsen</h1>
      <p class="holder-title">Diploma of Professional Pilates Instruction</p>
    </header>

    <ul class="contact">
      <li>
        <svg viewBox="0 0 11 11" aria-hidden="true"><rect x="2.5" y="0.5" width="6" height="10" rx="1" fill="none" stroke="#dc4d66" stroke-width="1"/><line x1="4.5" y1="8.8" x2="6.5" y2="8.8" stroke="#dc4d66" stroke-width="1"/></svg>
        <span>041 000 7392</span>
      </li>
      <li>
        <svg viewBox="0 0 11 11" aria-hidden="true"><rect x="0.5" y="2" width="10" height="7" fill="none" stroke="#dc4d66" stroke-width="1"/><polyline points="0.5,2 5.5,6 10.5,2" fill="none" stroke="#dc4d66" stroke-width="1"/></svg>
        <span>info@motionnest.com.au</span>
      </li>
    </ul>

    <address class="studio">
      <div class="studio-label">Studio location</div>
      <div>12 Kestrel Avenue</div>
      <div>Brookmere WA 6020</div>
    </address>

    <div class="front-mark">
      <span class="brand-dot"></span>
      <span class="front-mark-name">Motion Nest</span>
    </div>

    <div class="rule rule--long"></div>
    <span class="website">www.motionnest.com.au</span>
    <div class="rule rule--short"></div>
  </section>

</main>
</body>
</html>
```